Handelsunternehmen für haltbare Lebensmittel benötigt Webdesign
Zielgruppe
Wir sind ein Hamburger Handelsunternehmen für haltbare Lebensmittel.
Durch diese Website soll ein Interesse geweckt werden zur Zusammenarbeit und womöglich zur Kooperation der verschiedensten Großhändler des Food-Sektors mit der Vornalto GmbH. Endverbraucher können sich aufgrund der Entdeckung unseres Firmennamens informieren wer wir sind und was wir machen.
Aufgabenstellung
Bitte unterstützt uns bei der Erstellung einer Website unserer Unternehmen. Diese Website soll für unsere Firma Vornalto GmbH sein. Bitte deshalb auch nur den Fokus auf Design für die vornalto.de Seite legen.
Ein externer Shop unter dem Namen kelmstrand.de der Produkte der Kelmstrand vertreibt soll zu einem späteren Zeitpunkt folgen. Dieser Link sollte zwingend im Design als link involviert sein.
Dem Anhang beigefügt findet Ihr unsere beiden Logos.
Da sich unsere zweite Marke Kelmstrand in Zukunft durch das Thema Hamburg optisch definieren soll, beachtet bitte das Vornalto themenübergreifend und generisch funktioniert.
Neu**********Um einen stimmungsvollen Gesamteindruck zu erzeugen im Banner, bitten wir um Verwendung moderner, natürlicher Bilder aus den Bereichen Frische und Natur. Durch florale Illustrationen sollen Akzente gesetzt werden und der Look aufgelockert sein.*************Neu
Unsere Zielgruppe sind erfahrene oder nichterfahrene kochbegeisterte Entdecker kulinarischer Genüsse die sich aufgrund der Entdeckung des Firmennamens auf unseren Artikeln des Kelmstrand Portfolios über die Herkunft des Unternehmens informieren möchten. Die Zielgruppe zeichnet sich durch Spontanität und Individualität aus. Werbung gegenüber ist die Zielgruppe sehr aufgeschlossen. Beim Einkauf ist ihnen Qualität wichtiger als der Preis. Sie konsumieren gerne Markenartikel und bevorzugen beim Einkauf eine Inspiration die wir Ihnen über die Website mitgeben werden. Die Umweltverträglichkeit von Produkten spielt für sie eine große Rolle. Nachhaltigkeit ist ihnen wichtig.
Wir wünschen uns einen hohen Wiedererkennungswert der durch unseren internationalen Namen begründet ist und einer europaweiten Expansion nichts im Wege steht.
Es soll ein OnePager werden der auch in der Mobilversion gut funktionieren muss. Also muss die Responsivität sehr gut umgesetzt sein.
Der Firmenauftritt soll grob wie folgt aufgebaut sein:
Home
LOGO(De..

```html
<!DOCTYPE html>
<html lang="de">
<head>
<meta charset="utf-8">
<title>Vornalto</title>
<link rel="stylesheet" href="https://fonts.googleapis.com/css2?family=Montserrat:wght@400;500;600;700;800&display=swap">
<style>
  :root{
    --ink:#1c1d22;
    --white:#ffffff;
    --gold:#f2b420;
    --gold-line:#b88a1a;
    --text:#1a1a1a;
    --card-line:#dfe3e8;
    --ring:#e3e9ef;
    --mist:#cfd9e2;
    --field:#f4f6f8;
    --placeholder:#6b6f75;
    --blue:#1f4fa0;
    --grey:#8d8f94;
    --plate:#1f272a;
  }
  *{box-sizing:border-box;margin:0;padding:0}
  html,body{width:1200px;height:2807px;overflow:hidden}
  body{position:relative;font-family:"Montserrat",sans-serif;color:var(--text);background:var(--white)}
  .abs{position:absolute}

  /* hero */
  .hero{left:0;top:0;width:1200px;height:676px;
    background:radial-gradient(ellipse at 88% 30%,#6b5a1e 0%,transparent 30%),
               radial-gradient(ellipse at 95% 8%,#7a1b14 0%,transparent 18%),
               radial-gradient(ellipse at 12% 75%,#2d4a22 0%,transparent 25%),
               radial-gradient(ellipse at 60% 85%,#5a4b1a 0%,transparent 18%),
               radial-gradient(ellipse at 28% 83%,#6a6320 0%,transparent 10%),
               linear-gradient(180deg,#1e2226,#15181b)}
  .topbar{left:111px;top:14px;width:977px;height:24px;color:var(--white);font-size:11px;display:flex;align-items:center;justify-content:space-between}
  .search{display:flex;align-items:center;gap:22px;letter-spacing:.5px}
  .mail{display:flex;align-items:center;gap:7px}
  .nav{left:111px;top:56px;width:977px;height:44px;border-top:1px solid rgba(255,255,255,.8);border-bottom:1px solid rgba(255,255,255,.8);display:flex}
  .nav a{color:var(--white);text-decoration:none;font-size:13px;font-weight:500;letter-spacing:1.5px;display:flex;align-items:center;justify-content:center;border-right:1px solid rgba(255,255,255,.8)}
  .nav a:last-child{border-right:none}
  .wreath{left:342px;top:205px;width:520px;height:190px;border-radius:95px;
    background:radial-gradient(ellipse at 50% 50%,rgba(255,255,255,.30) 0%,rgba(255,255,255,.18) 55%,rgba(255,255,255,0) 72%)}
  .logo-plate{left:392px;top:256px;width:415px;height:93px;background:var(--plate);display:flex;align-items:center;justify-content:center}
  .logo-plate span{font-size:62px;font-weight:800;color:var(--white);letter-spacing:2px}

  /* welcome */
  .welcome{left:0;top:676px;width:1200px;height:465px;background:var(--ink)}
  .welcome-box{left:111px;top:85px;width:977px;height:294px;border:1px solid var(--gold-line);color:var(--white);text-align:center;padding:34px 56px 0}
  .welcome-box h2{font-size:35px;font-weight:700;margin-bottom:18px}
  .welcome-box p{font-size:13.6px;line-height:20.6px;font-weight:500;margin-bottom:20px}

  /* portfolio */
  .portfolio-title{left:0;top:1218px;width:1200px;text-align:center;font-size:35px;font-weight:700}
  .card{width:225px;height:328px;border:1px solid var(--card-line);background:var(--white)}
  .card .photo{position:absolute;left:30px;top:42px;width:164px;height:164px;border-radius:50%;border:5px solid var(--ring)}
  .card h3{position:absolute;left:0;top:226px;width:100%;text-align:center;font-size:18px;font-weight:600}
  .card a{position:absolute;left:35px;top:263px;width:154px;height:31px;border:1.5px solid var(--gold);border-radius:16px;color:var(--gold);font-size:11.5px;font-weight:700;text-decoration:none;display:flex;align-items:center;justify-content:center}

  /* contact */
  .contact{left:0;top:2065px;width:1200px;height:560px;background:var(--mist);overflow:hidden}
  .spices-left{left:0;top:0;width:327px;height:560px;background:radial-gradient(ellipse at 30% 40%,#6b3a26 0%,#8a5a3a 30%,rgba(207,217,226,0) 75%)}
  .spices-right{left:861px;top:60px;width:339px;height:500px;background:radial-gradient(ellipse at 70% 65%,#b8352a 0%,#c4633a 25%,#e8e8e8 45%,rgba(207,217,226,0) 75%)}
  .contact h2{left:0;top:76px;width:1200px;text-align:center;font-size:35px;font-weight:700}
  .contact .lead{left:0;top:126px;width:1200px;text-align:center;font-size:14px;font-weight:500;color:#333}
  .field{background:var(--field);border-radius:6px;width:233px;height:46px;font-size:14px;color:var(--placeholder);padding:13px 16px}
  .field.message{width:485px;height:114px}
  .submit{left:543px;top:432px;width:117px;height:41px;background:var(--gold);border-radius:21px;color:var(--white);font-size:14px;letter-spacing:1.2px;display:flex;align-items:center;justify-content:center}

  /* footer */
  .footer{left:0;top:2625px;width:1200px;height:182px;background:var(--ink);color:var(--white)}
  .f-item{left:111px;display:flex;align-items:center;gap:9px;font-size:12px;font-weight:500}
  .f-logo{left:0;top:70px;width:1200px;text-align:center;font-size:38px;font-weight:800;letter-spacing:1px}
  .social{top:73px;width:27px;height:27px;border-radius:50%;background:var(--blue);display:flex;align-items:center;justify-content:center}
</style>
</head>
<body>

<header class="abs hero" role="img" aria-label="Dunkler Tisch mit Gewürzschalen, Olivenöl, Pesto, Basilikum und Pasta"></header>

<div class="abs topbar">
  <div class="search">
    <svg width="15" height="15" viewBox="0 0 15 15"><circle cx="6" cy="6" r="5" fill="none" stroke="#fff" stroke-width="1.6"/><line x1="9.8" y1="9.8" x2="14" y2="14" stroke="#fff" stroke-width="1.6"/></svg>
    <span>SEARCH . . .</span>
  </div>
  <div class="mail">
    <svg width="12" height="9" viewBox="0 0 12 9"><rect x=".5" y=".5" width="11" height="8" fill="none" stroke="#fff"/><polyline points=".5,.5 6,5 11.5,.5" fill="none" stroke="#fff"/></svg>
    <span>info@vornalto.com</span>
  </div>
</div>

<nav class="abs nav">
  <a href="#home" style="width:238px">Home</a>
  <a href="#portfolio" style="width:251px">Portfolio</a>
  <a href="https://kelmstrand.de" style="width:249px">Online Shop</a>
  <a href="#kontakt" style="width:239px">Kontakt</a>
</nav>

<div class="abs wreath" role="img" aria-label="Weißer floraler Blätterkranz um das Logo"></div>
<div class="abs logo-plate"><span>VORNALTO</span></div>

<section class="abs welcome">
  <div class="abs welcome-box">
    <h2>Willkommen</h2>
    <p>But I must explain to you how all this mistaken idea of denouncing pleasure and praising pain was born and I will give you a complete account of the system, and expound the actual teachings of the great explorer of the truth, the master-builder of human happiness. No one rejects, dislikes, or avoids pleasure itself, because it is pleasure, but because those who do not know how to pursue pleasure rationally encounter consequences that are extremely painful.</p>
    <p>Nor again is there anyone who loves or pursues or desires to obtain pain of itself, because it is pain, but because occasionally circumstances occur in which toil and pain can procure him some great pleasure. To take a trivial example, which of us ever undertakes laborious physical exercise, except to obtain some advantage from it</p>
  </div>
</section>

<h2 class="abs portfolio-title" id="portfolio">Portfolio</h2>

<div class="abs card" style="left:111px;top:1296px"><div class="photo" role="img" aria-label="Safranfäden" style="background:radial-gradient(circle,#b3221c,#7d1410 60%,#fff 62%)"></div><h3>Safran</h3><a href="#">MEER INFORMATIE</a></div>
<div class="abs card" style="left:362px;top:1296px"><div class="photo" role="img" aria-label="Gewürze in Holzschaufeln" style="background:radial-gradient(circle,#d07a2a,#b08a5a 55%,#fff 70%)"></div><h3>Gewürze</h3><a href="#">MEER INFORMATIE</a></div>
<div class="abs card" style="left:613px;top:1296px"><div class="photo" role="img" aria-label="Trockenfrüchte" style="background:radial-gradient(circle,#f08a1a,#5a2a3a 60%,#fff 72%)"></div><h3>Trockenfrüchte</h3><a href="#">MEER INFORMATIE</a></div>
<div class="abs card" style="left:863px;top:1296px"><div class="photo" role="img" aria-label="Kräuter mit Mörser" style="background:radial-gradient(circle,#3a3f48,#3f7a2a 50%,#fff 72%)"></div><h3>Kräuter</h3><a href="#">MEER INFORMATIE</a></div>

<div class="abs card" style="left:111px;top:1651px"><div class="photo" role="img" aria-label="Pistazien" style="background:radial-gradient(circle,#9aaa4a,#c79a6a 45%,#fff 65%)"></div><h3>Pistazien</h3><a href="#">MEER INFORMATIE</a></div>
<div class="abs card" style="left:362px;top:1651px"><div class="photo" role="img" aria-label="Teeblätter mit Minze" style="background:radial-gradient(circle,#4a4a3e,#4a8a3a 55%,#fff 72%)"></div><h3>Tee</h3><a href="#">MEER INFORMATIE</a></div>
<div class="abs card" style="left:613px;top:1651px"><div class="photo" role="img" aria-label="Sonnenblume und Öl" style="background:radial-gradient(circle,#f2c21a,#e0a010 50%,#fff 72%)"></div><h3>Öl</h3><a href="#">MEER INFORMATIE</a></div>
<div class="abs card" style="left:863px;top:1651px"><div class="photo" role="img" aria-label="Reiskörner" style="background:radial-gradient(circle,#f4f4f2,#dcdcd8 60%,#fff 75%)"></div><h3>Reis</h3><a href="#">MEER INFORMATIE</a></div>

<section class="abs contact" id="kontakt">
  <div class="abs spices-left" role="img" aria-label="Nelken, Piment und Chili"></div>
  <div class="abs spices-right" role="img" aria-label="Gewürzschalen mit Chili und Sternanis"></div>
  <h2 class="abs">Kontakt</h2>
  <p class="abs lead">Lorem Ipsum is simply dummy text of the printing and typesetting</p>
  <div class="abs field" style="left:359px;top:172px">Name:</div>
  <div class="abs field" style="left:611px;top:172px">Email:</div>
  <div class="abs field" style="left:359px;top:235px">Phone:</div>
  <div class="abs field" style="left:611px;top:235px">Company:</div>
  <div class="abs field message" style="left:359px;top:299px">Message:</div>
  <div class="abs submit">SUBMIT</div>
</section>

<footer class="abs footer">
  <div class="abs f-item" style="top:42px"><svg width="10" height="13" viewBox="0 0 10 13"><path d="M5 0a5 5 0 0 0-5 5c0 3.5 5 8 5 8s5-4.5 5-8a5 5 0 0 0-5-5z" fill="#f2b420"/><circle cx="5" cy="5" r="1.8" fill="#1c1d22"/></svg><span>27 Kelmweg 14, 20457 Hamburg</span></div>
  <div class="abs f-item" style="top:68px"><svg width="10" height="8" viewBox="0 0 12 9"><rect x=".5" y=".5" width="11" height="8" fill="none" stroke="#f2b420"/><polyline points=".5,.5 6,5 11.5,.5" fill="none" stroke="#f2b420"/></svg><span>info@vornalto.com</span></div>
  <div class="abs f-item" style="top:94px"><svg width="10" height="10" viewBox="0 0 10 10"><path d="M2 0l2 2.5-1 1.2c.6 1.3 1.7 2.4 3 3l1.2-1L10 8l-1.5 2C4 10 0 6 0 1.5z" fill="#f2b420"/></svg><span>040-555-0142</span></div>
  <div class="abs f-item" style="top:122px"><svg width="10" height="10" viewBox="0 0 10 10"><rect x="0" y="3" width="10" height="6" rx="1" fill="#f2b420"/><rect x="2" y="0" width="6" height="3" fill="#f2b420"/></svg><span>040-555-0143</span></div>
  <div class="abs f-logo">VORNALTO</div>
  <div class="abs social" style="left:923px;background:var(--grey)"><svg width="8" height="5" viewBox="0 0 8 5"><polyline points="1,4 4,1 7,4" fill="none" stroke="#fff" stroke-width="1.4"/></svg></div>
  <div class="abs social" style="left:958px" aria-label="Soziales Netzwerk"></div>
  <div class="abs social" style="left:992px" aria-label="Soziales Netzwerk"></div>
  <div class="abs social" style="left:1027px" aria-label="Soziales Netzwerk"></div>
  <div class="abs social" style="left:1061px;background:var(--gold)" aria-label="Soziales Netzwerk"></div>
</footer>

</body>
</html>
```